Quorvan Stationery Design Project

We need stationary design that goes with the attached logo. We have logo in two different versions. One in Red/Black and the other in Blue/Green. Red/Black is going to be our primary color and we are planning to use Blue/Green occasionally as necessary.

So we need stationary design in both color combinations. Maybe you can work with Red/Black first and once we decide on the design, then you can show the Blue/Green variation.

Please see the attached png and psd files for logo.

Target Market(s)

IT departments of Medium size Enterprises.

Industry/Entity Type

Work

Requirements
Must have
• -Letter head
-Cover page design for white papers and articles that are going to publish
-Business Card
-Envelope design
Nice to have
• - High level design template that we can follow for our internal web applications

```html
<!DOCTYPE html>
<html lang="en">
<head>
<meta charset="utf-8">
<title>Quorvan Software Stationery</title>
<link href="https://fonts.googleapis.com/css2?family=Lato:wght@400;700&display=swap" rel="stylesheet">
<style>
:root{
  --canvas:#b1b2b4;
  --paper:#f0f0f2;
  --red:#d8060c;
  --red-deep:#a30d14;
  --ink:#1b1b1b;
  --grey-text:#6d6d6d;
}
*{box-sizing:border-box;margin:0;padding:0}
html,body{width:1200px;height:1133px;overflow:hidden}
body{background:var(--canvas);font-family:'Lato',sans-serif;color:var(--ink);position:relative}
.sheet{position:absolute;background:var(--paper);overflow:hidden;box-shadow:0 0 2px rgba(0,0,0,.15)}
.red-sheet{background:radial-gradient(circle at 50% 45%,var(--red) 0%,var(--red-deep) 80%)}
.wordmark{font-weight:700;color:var(--ink);letter-spacing:.18em;text-transform:uppercase;line-height:1.15;display:flex;align-items:center;gap:.5em}
.wordmark .mark-square{width:1.4em;height:1.4em;background:var(--red);flex:none}
.wordmark.light{color:#fff}
.wordmark.light .mark-square{background:#fff}
.swoosh{position:absolute;left:0;bottom:0;width:100%}
/* cover – title */
.cover-title{left:57px;top:57px;width:357px;height:506px}
.cover-title .wordmark{position:absolute;right:28px;top:30px;font-size:12px}
.cover-title h1{position:absolute;top:188px;width:100%;text-align:center;font-weight:400;font-size:13px}
.cover-title .rule{position:absolute;left:0;width:100%;height:2px;background:var(--ink)}
.cover-title .band{position:absolute;left:0;top:217px;width:100%;height:73px;background:radial-gradient(ellipse at 55% 50%,var(--red) 0%,var(--red-deep) 75%);padding:18px 0 0 39px}
.cover-title .band p{color:#fff;font-size:7px;line-height:11px}
.cover-title .footer-line{position:absolute;bottom:14px;width:100%;text-align:center;font-size:5px;line-height:7px;color:var(--grey-text)}
/* covers */
.cover-red{left:421px;top:57px;width:358px;height:506px;display:flex;align-items:center;justify-content:center}
.cover-red .wordmark{font-size:20px;margin-top:-40px}
.cover-white{left:787px;top:57px;width:358px;height:506px;display:flex;align-items:center;justify-content:center}
.cover-white .wordmark{font-size:20px;margin-top:-40px}
/* letterhead */
.letterhead{left:57px;top:570px;width:357px;height:507px}
.letterhead .wordmark{position:absolute;left:24px;top:28px;font-size:10px}
.letterhead .contact{position:absolute;top:28px;font-size:5px;line-height:6.5px;color:var(--ink)}
.letterhead .contact.address{left:212px;padding-left:8px}
.letterhead .contact.lines{left:284px;padding-left:8px;border-left:1px solid #bbb}
.icon-dot{display:inline-block;width:4px;height:4px;border-radius:50%;background:var(--red);margin-right:3px;vertical-align:middle}
.letterhead .letter{position:absolute;left:32px;top:117px;width:300px;font-size:6.4px;line-height:9px;color:var(--grey-text)}
.letterhead .letter p{margin-bottom:9px}
.letterhead .signature{width:70px;height:26px;background:linear-gradient(90deg,#e4e6f0,#d9dcec);margin-top:14px}
/* envelopes */
.envelope-back{left:421px;top:712px;width:390px;height:179px}
.envelope-back .flap-mark{position:absolute;left:50%;top:18px;transform:translateX(-50%);width:16px;height:16px;background:#fff}
.envelope-front{left:421px;top:900px;width:390px;height:177px}
.envelope-front .wordmark{position:absolute;left:18px;top:22px;font-size:8px}
.envelope-front .return{position:absolute;left:45px;top:46px;font-size:5px;line-height:6px}
/* cards */
.card-front{left:837px;top:712px;width:308px;height:177px}
.card-front .wordmark{position:absolute;left:30px;top:74px;font-size:11px}
.card-front .person{position:absolute;left:175px;top:24px;padding-left:6px;border-left:1px solid #d0d0d0;height:120px}
.card-front .name{color:var(--red);font-size:12px;font-weight:400;letter-spacing:.02em}
.card-front .role{font-size:7px;margin-bottom:14px}
.card-front .detail{font-size:7px;line-height:9.5px}
.card-front .detail .icon-dot{width:5px;height:5px}
.card-back{left:837px;top:900px;width:308px;height:177px;display:flex;flex-direction:column;align-items:center;justify-content:center}
.card-back .mark-square{width:40px;height:40px;background:#fff;margin-top:-10px}
.card-back .url{position:absolute;bottom:16px;color:#fff;font-size:8px;letter-spacing:.25em}
</style>
</head>
<body>

<section class="sheet cover-title">
  <div class="wordmark"><span class="mark-square"></span><span>Quorvan<br>Software</span></div>
  <h1>Title Line Title Line</h1>
  <div class="rule" style="top:210px"></div>
  <div class="band"><p>Title Line Title Line</p><p>Title Line Title Line</p><p>Title Line Title Line</p></div>
  <div class="rule" style="top:294px"></div>
  <div class="footer-line">27 Linden Park Road, Suite 310, Fairhaven, New York 11062<br>Phone : + 000 0000 0000 &nbsp;|&nbsp; Fax : + 000 0000 0000 &nbsp;|&nbsp; Email : info@quorvan.com &nbsp;|&nbsp; www.quorvan.com</div>
</section>

<section class="sheet red-sheet cover-red">
  <div class="wordmark light"><span class="mark-square"></span><span>Quorvan<br>Software</span></div>
</section>

<section class="sheet cover-white">
  <div class="wordmark"><span class="mark-square"></span><span>Quorvan<br>Software</span></div>
</section>

<section class="sheet letterhead">
  <div class="wordmark"><span class="mark-square"></span><span>Quorvan<br>Software</span></div>
  <div class="contact address"><span class="icon-dot"></span>27 Linden Park Road<br>Suite 310, Fairhaven<br>New York 11062</div>
  <div class="contact lines">
    <span class="icon-dot"></span>+ 000 000 0000<br>
    <span class="icon-dot"></span>+ 000 000 0000<br>
    <span class="icon-dot"></span>info@quorvan.com<br>
    <span class="icon-dot"></span>www.quorvan.com
  </div>
  <div class="letter">
    <p>Someone Some body<br>52 Elm Row<br>Carrowick, Australia</p>
    <p>Dear Someone Somebody,</p>
    <p>Lorem ipsum dolor sit amet, consectetuer adipiscing elit, sed diam nonummy nibh euismod tincidunt ut laoreet dolore magna aliquam erat volutpat. Ut wisi enim ad minim veniam, quis nostrud exerci tation ullamcorper suscipit lobortis nisl ut aliquip ex ea commodo consequat. Duis autem vel eum iriure dolor in hendrerit in vulputate velit esse molestie consequat, vel illum dolore eu feugiat nulla facilisis at vero eros et accumsan et iusto odio dignissim qui blandit praesent luptatum zzril delenit augue duis dolore te feugait nulla facilisi.</p>
    <p>Lorem ipsum dolor sit amet, consectetuer adipiscing elit, sed diam nonummy nibh euismod tincidunt ut laoreet dolore magna aliquam erat volutpat. Ut wisi enim ad minim veniam, quis nostrud exerci tation ullamcorper suscipit lobortis nisl ut aliquip ex ea commodo consequat. Duis autem vel eum iriure dolor in hendrerit in vulputate velit esse molestie consequat, vel illum dolore eu feugiat nulla facilisis at vero eros et accumsan et iusto odio dignissim qui blandit praesent luptatum zzril delenit augue duis dolore te feugait nulla facilisi.</p>
    <p>Lorem ipsum dolor sit amet, consectetuer adipiscing elit, sed diam nonummy nibh euismod tincidunt ut laoreet dolore magna aliquam erat volutpat. Ut wisi enim ad minim veniam, quis nostrud exerci tation ullamcorper suscipit lobortis nisl ut aliquip ex ea commodo consequat. Duis autem vel eum iriure dolor in hendrerit in vulputate velit esse molestie consequat, vel illum dolore eu feugiat nulla facilisis at vero eros et accumsan et iusto odio dignissim qui blandit praesent luptatum zzril delenit augue duis dolore te feugait nulla facilisi.</p>
    <p>Youre Sincerely,<br>Owen Carter.</p>
    <div class="signature" role="img" aria-label="Handwritten signature"></div>
  </div>
  <svg class="swoosh" width="357" height="70" viewBox="0 0 357 70" preserveAspectRatio="none">
    <defs>
      <linearGradient id="greyFade" x1="0" x2="1"><stop offset="0" stop-color="#d9d9db"/><stop offset="1" stop-color="#3d3e42"/></linearGradient>
    </defs>
    <path d="M0,58 Q200,55 357,10 L357,26 Q210,64 0,64 Z" fill="url(#greyFade)"/>
    <path d="M0,62 Q210,64 357,28 L357,70 L0,70 Z" fill="var(--red)"/>
  </svg>
</section>

<section class="sheet envelope-back">
  <svg width="390" height="60" viewBox="0 0 390 60" preserveAspectRatio="none" style="position:absolute;top:0;left:0">
    <path d="M0,0 L390,0 L390,10 Q300,38 195,56 Q90,38 0,10 Z" fill="var(--red)"/>
    <path d="M250,30 Q320,16 390,6 M260,33 Q325,19 390,10" stroke="#f28a8a" stroke-width=".6" fill="none"/>
  </svg>
  <div class="flap-mark"></div>
</section>

<section class="sheet envelope-front">
  <div class="wordmark"><span class="mark-square"></span><span>Quorvan<br>Software</span></div>
  <div class="return">27 Linden Park Road<br>Suite 310, Fairhaven<br>New York 11062</div>
  <svg class="swoosh" width="390" height="75" viewBox="0 0 390 75" preserveAspectRatio="none">
    <defs>
      <linearGradient id="greyFade2" x1="0" x2="1"><stop offset="0" stop-color="#e2e2e4"/><stop offset="1" stop-color="#3d3e42"/></linearGradient>
    </defs>
    <path d="M0,60 Q220,58 390,6 L390,22 Q230,68 0,68 Z" fill="url(#greyFade2)"/>
    <path d="M0,66 Q230,68 390,24 L390,75 L0,75 Z" fill="var(--red)"/>
  </svg>
</section>

<section class="sheet card-front">
  <div class="wordmark"><span class="mark-square"></span><span>Quorvan<br>Software</span></div>
  <div class="person">
    <div class="name">MARTIN HALE</div>
    <div class="role">President</div>
    <div class="detail"><span class="icon-dot"></span>27 Linden Park Road<br>&nbsp;&nbsp;&nbsp;Suite 310, Fairhaven<br>&nbsp;&nbsp;&nbsp;New York 11062</div>
    <div class="detail" style="margin-top:5px">
      <span class="icon-dot"></span>+ 000 000 0000<br>
      <span class="icon-dot"></span>+ 000 000 0000<br>
      <span class="icon-dot"></span>+ 000 000 0000<br>
      <span class="icon-dot"></span>martin@quorvan.com<br>
      <span class="icon-dot"></span>www.quorvan.com
    </div>
  </div>
  <svg class="swoosh" width="308" height="55" viewBox="0 0 308 55" preserveAspectRatio="none">
    <defs>
      <linearGradient id="greyFade3" x1="0" x2="1"><stop offset="0" stop-color="#3d3e42"/><stop offset=".6" stop-color="#8a8b8f"/><stop offset="1" stop-color="#e0e0e2"/></linearGradient>
    </defs>
    <path d="M0,2 Q110,42 308,40 L308,46 Q110,50 0,18 Z" fill="url(#greyFade3)"/>
    <path d="M0,18 Q110,50 308,44 L308,55 L0,55 Z" fill="var(--red)"/>
  </svg>
</section>

<section class="sheet red-sheet card-back">
  <div class="mark-square"></div>
  <div class="url">www.quorvansoftware.com</div>
</section>

</body>
</html>
```